Custom Label for Essential Oils Bottle

We are a brand new company who specializes in seeking 100% pure essential oils. You would need to create a label that is similar to the designs attached, but unique to us. Our favorite label design is by quiet harbor blends. We really like how elegant their look is and would like to model that.
We will give the exact text of what we need put into the label to the winner after our favorite design is selected. Also, our logo is attached.
We would like the whole line to follow the same design with minor or tweaks for each scent (different color and text is all).
The label size would be 3" x 1.125" . There will be approximately 60 different oils in our first line but we only need 6 created for our first run.
Attached are the logo designs we really like.
Our first scent will be for a "Lemon" Essential oil bottle so design accordingly. The additional scents will be clove bud , peppermint, sweet orange, rosemary, and eucalyptus.
Thanks so much, and I look forward to seeing your designs!
Sam
Target Market(s)
Women, ages 18-65, wealthy
Industry/Entity Type
It Company

```html
<!DOCTYPE html>
<html lang="en">
<head>
<meta charset="utf-8">
<title>Lumen Grove – Essential Oil Labels</title>
<link href="https://fonts.googleapis.com/css2?family=Oswald:wght@300;400&display=swap" rel="stylesheet">
<style>
  :root {
    --page: #ffffff;
    --eucalyptus: #bfe0ec;
    --rosemary: #f5c6d0;
    --lemon: #b9e0d5;
    --ink: #8b8b8b;
    --brand: #6a5646;
    --leaf-eucalyptus: #9fcbdc;
    --leaf-rosemary: #e8a9b7;
    --leaf-lemon: #97cdbd;
    --rule: #ffffff;
  }
  * { margin: 0; padding: 0; box-sizing: border-box; }
  html, body {
    width: 1200px;
    height: 869px;
    overflow: hidden;
    background: var(--page);
  }
  .canvas {
    position: relative;
    width: 1200px;
    height: 869px;
  }
  .label {
    position: absolute;
    top: 436px;
    width: 172px;
    height: 278px;
    overflow: hidden;
    font-family: "Oswald", sans-serif;
    color: var(--ink);
  }
  .label--eucalyptus { left: 155px; background: var(--eucalyptus); }
  .label--rosemary   { left: 392px; background: var(--rosemary); }
  .label--lemon      { left: 794px; background: var(--lemon); }

  .brand {
    position: absolute;
    top: 22px;
    left: 0;
    right: 0;
    text-align: center;
    font-weight: 400;
    font-size: 17px;
    line-height: 1;
    color: var(--brand);
    letter-spacing: 0.02em;
  }
  .brand-sub {
    display: block;
    margin-top: 5px;
    font-weight: 300;
    font-size: 7px;
    letter-spacing: 0.12em;
    text-transform: uppercase;
  }
  .scent {
    position: absolute;
    top: 80px;
    left: 14px;
    font-weight: 300;
    font-size: 31px;
    line-height: 1;
    text-transform: uppercase;
    letter-spacing: 0.01em;
    white-space: nowrap;
  }
  .kind, .purity {
    position: absolute;
    left: 16px;
    font-weight: 300;
    font-size: 10px;
    text-transform: uppercase;
    letter-spacing: 0.04em;
  }
  .kind { top: 120px; }
  .purity { top: 140px; }
  .rule {
    position: absolute;
    left: 16px;
    width: 60px;
    height: 1px;
    background: var(--rule);
  }
  .rule--upper { top: 137px; }
  .rule--lower { top: 158px; }
  .volume {
    position: absolute;
    left: 16px;
    bottom: 26px;
    font-weight: 300;
    font-size: 11px;
  }
  .botanical {
    position: absolute;
    right: 0;
    bottom: 0;
    width: 62px;
    height: 120px;
    border-top-left-radius: 40px;
  }
  .label--eucalyptus .botanical { background: linear-gradient(160deg, var(--eucalyptus), var(--leaf-eucalyptus)); }
  .label--rosemary .botanical   { background: linear-gradient(160deg, var(--rosemary), var(--leaf-rosemary)); }
  .label--lemon .botanical      { background: linear-gradient(160deg, var(--lemon), var(--leaf-lemon)); }
</style>
</head>
<body>
<main class="canvas">

  <section class="label label--eucalyptus">
    <p class="brand">Lumen Grove<span class="brand-sub">Essential Oils</span></p>
    <h2 class="scent">Eucalyptus.</h2>
    <p class="kind">Essential Oil</p>
    <span class="rule rule--upper"></span>
    <p class="purity">100% Pure</p>
    <span class="rule rule--lower"></span>
    <p class="volume">15ml</p>
    <div class="botanical" role="img" aria-label="Fine line drawing of eucalyptus leaves"></div>
  </section>

  <section class="label label--rosemary">
    <p class="brand">Lumen Grove<span class="brand-sub">Essential Oils</span></p>
    <h2 class="scent">Rosemary</h2>
    <p class="kind">Essential Oil</p>
    <span class="rule rule--upper"></span>
    <p class="purity">100% Pure</p>
    <span class="rule rule--lower"></span>
    <p class="volume">15ml</p>
    <div class="botanical" role="img" aria-label="Fine line drawing of rosemary sprigs"></div>
  </section>

  <section class="label label--lemon">
    <p class="brand">Lumen Grove<span class="brand-sub">Essential Oils</span></p>
    <h2 class="scent">Lemon</h2>
    <p class="kind">Essential Oil</p>
    <span class="rule rule--upper"></span>
    <p class="purity">100% Pure</p>
    <span class="rule rule--lower"></span>
    <p class="volume">15ml</p>
    <div class="botanical" role="img" aria-label="Fine line drawing of lemon leaves"></div>
  </section>

</main>
</body>
</html>
```